Lantern Hearthworks Business Cards

Looking to create simple business cards that highlight our unique three sided triangle fire pit design with the colors and font of our logo, listed below.

Requirements
Must have
• Looking for something simple that includes a picture of our fire pit with name, website (lanternhearthworks.com), phone number and email. Want to keep the color mostly orange and black.
• Font is gotham(medium) and orange color code is #ee6e22

```html
<!DOCTYPE html>
<html lang="en">
<head>
<meta charset="UTF-8">
<title>Lantern Hearthworks Business Cards</title>
<link href="https://fonts.googleapis.com/css2?family=Montserrat:wght@500;600&family=Raleway:wght@600&family=Arimo&display=swap" rel="stylesheet">
<style>
  :root {
    --backdrop: #595959;
    --card-white: #ffffff;
    --brand-orange: #ee6e22;
    --ink: #1f1f1f;
    --gravel-dark: #1e1e1e;
    --gravel-mid: #4a4a4a;
    --ember: #f07a1e;
  }
  * { margin: 0; padding: 0; box-sizing: border-box; }
  html, body {
    width: 1200px;
    height: 900px;
    overflow: hidden;
    background: var(--backdrop);
  }
  .canvas {
    position: relative;
    width: 1200px;
    height: 900px;
  }
  .card {
    position: absolute;
    top: 200px;
    width: 310px;
    height: 502px;
    box-shadow: 3px 4px 6px rgba(0, 0, 0, 0.45);
    overflow: hidden;
  }
  .card-front {
    left: 253px;
    background: var(--card-white);
    border-radius: 52px 0 52px 0;
  }
  .card-back {
    left: 627px;
    border-radius: 0 52px 0 52px;
  }
  .brand-name {
    position: absolute;
    top: 178px;
    left: 0;
    width: 100%;
    text-align: center;
    font-family: "Montserrat", sans-serif;
    font-weight: 500;
    color: var(--brand-orange);
    line-height: 1.05;
  }
  .brand-name .line-one {
    display: block;
    font-size: 31px;
    letter-spacing: 4px;
  }
  .brand-name .line-two {
    display: block;
    font-size: 25px;
    letter-spacing: 1.5px;
  }
  .person-name {
    position: absolute;
    top: 341px;
    left: 34px;
    font-family: "Raleway", sans-serif;
    font-weight: 600;
    font-size: 17.5px;
    color: var(--brand-orange);
    letter-spacing: 0.2px;
  }
  .contact-list {
    position: absolute;
    top: 393px;
    left: 33px;
    list-style: none;
    font-family: "Arimo", Arial, sans-serif;
    font-size: 14px;
    color: var(--ink);
  }
  .contact-list li {
    display: flex;
    align-items: center;
    height: 19px;
  }
  .contact-icon {
    width: 16px;
    height: 16px;
    margin-right: 6px;
    flex: none;
  }
  .fire-pit-photo {
    width: 100%;
    height: 100%;
    background:
      radial-gradient(ellipse 90px 60px at 62% 50%, rgba(240, 122, 30, 0.85), rgba(240, 122, 30, 0) 100%),
      radial-gradient(ellipse 120px 150px at 55% 55%, rgba(10, 10, 10, 0.9), rgba(10, 10, 10, 0) 100%),
      radial-gradient(circle at 30% 20%, var(--gravel-mid), var(--gravel-dark) 80%);
  }
</style>
</head>
<body>
<main class="canvas">
  <section class="card card-front" aria-label="Business card front">
    <h1 class="brand-name">
      <span class="line-one">LANTERN</span>
      <span class="line-two">HEARTHWORKS</span>
    </h1>

    <p class="person-name">MARCUS HALE</p>

    <ul class="contact-list">
      <li>
        <svg class="contact-icon" viewBox="0 0 16 16" aria-hidden="true">
          <rect x="1" y="1" width="14" height="14" rx="2" fill="none" stroke="#ee6e22" stroke-width="1.6"/>
          <path d="M5 4.2c.6-.4 1-.3 1.3.2l.7 1.3c.2.4.1.7-.2 1l-.5.4c.4.9 1.1 1.6 2 2l.4-.5c.3-.3.6-.4 1-.2l1.3.7c.5.3.6.7.2 1.3-.6.8-1.4 1.1-2.4.7C6.8 10.4 5.6 9.2 4.9 7.2c-.4-1 0-2.3.1-3z" fill="#ee6e22"/>
        </svg>
        044-555 018 274
      </li>
      <li>
        <svg class="contact-icon" viewBox="0 0 16 16" aria-hidden="true">
          <rect x="0.5" y="3" width="15" height="10" fill="#ee6e22"/>
          <path d="M0.5 3.3 8 9l7.5-5.7" fill="none" stroke="#ffffff" stroke-width="1.2"/>
        </svg>
        info@lanternhearthworks.com
      </li>
      <li>
        <svg class="contact-icon" viewBox="0 0 16 16" aria-hidden="true">
          <circle cx="8" cy="8" r="7.3" fill="#ee6e22"/>
          <g fill="none" stroke="#ffffff" stroke-width="0.9">
            <ellipse cx="8" cy="8" rx="3" ry="7.3"/>
            <line x1="8" y1="0.7" x2="8" y2="15.3"/>
            <line x1="0.7" y1="8" x2="15.3" y2="8"/>
            <path d="M2 4.3h12M2 11.7h12"/>
          </g>
        </svg>
        www.lanternhearthworks.com
      </li>
    </ul>
  </section>

  <section class="card card-back" aria-label="Business card back">
    <div class="fire-pit-photo" role="img" aria-label="Photo from above of a black steel triangular fire pit with burning logs and bright orange flames, set on dark gravel"></div>
  </section>
</main>
</body>
</html>
```